Our swimming pool service needs your help with letterhead

Letterhead for small swimming pool service- We would like a professional look with a creative layout- must be compatible with LedgerNest forms (sample attached)
No more than 2 colors in graphics

Target Market(s)

Homeowners/ Contractors

Font styles to use
Sans Serif

Colors
33a6d7
85cae6

Requirements
Must have
• Logo (file attached)
• Compatible with LedgerNest (sample attached)
• Mailing address- P.O. Box 58, Cedar Hollow NY 11592
• phone- (631) 529-6180
• email- marcdoylewater@mailbrook.net
• Licensed & Insured
Nice to have
• Small slogan- Examples:Family owned and operated for 25 years, 25 years of trusted service
• Creative layout
Should not have
• Blue color must be same as blue in our logo
• No thick lines of color
• No design in middle of page

```html
<!DOCTYPE html>
<html lang="en">
<head>
<meta charset="utf-8">
<title>Marc Doyle Pool Care – Letterhead</title>
<link href="https://fonts.googleapis.com/css2?family=Poppins:wght@400;500;600&family=Petit+Formal+Script&display=swap" rel="stylesheet">
<style>
  :root {
    --pool-light: #65ade0;
    --pool-dark: #1f3a5f;
    --ink: #222;
    --muted: #8c8c8c;
    --backdrop: #e7eaee;
    --paper: #ffffff;
  }
  * { box-sizing: border-box; margin: 0; padding: 0; }
  html, body { width: 1200px; height: 1200px; overflow: hidden; }
  body { background: var(--backdrop); font-family: "Poppins", sans-serif; color: var(--ink); position: relative; }

  .letterhead {
    position: absolute; left: 175px; top: 50px; width: 850px; height: 1100px;
    background: var(--paper); box-shadow: 0 6px 24px rgba(0,0,0,.15); overflow: hidden;
  }

  .brand { position: absolute; left: 36px; top: 46px; display: flex; align-items: center; gap: 10px; }
  .brand-dot { width: 30px; height: 30px; border-radius: 50%; background: var(--pool-light); }
  .brand-name { font-size: 28px; font-weight: 500; color: var(--pool-dark); letter-spacing: .5px; line-height: 1; }

  .contact { position: absolute; left: 535px; top: 48px; list-style: none; font-size: 13.5px; color: var(--pool-dark); }
  .contact li { display: flex; align-items: center; gap: 12px; height: 28px; }
  .contact svg { width: 11px; height: 11px; fill: var(--pool-dark); flex: none; }
  .licensed { position: absolute; left: 535px; top: 144px; font-weight: 600;
    font-size: 13px; letter-spacing: 4.6px; color: var(--pool-dark); }

  .recipient { position: absolute; left: 32px; top: 228px; }
  .recipient .to { font-size: 15px; }
  .recipient .name { font-size: 21px; letter-spacing: .8px; margin-top: 2px; }
  .recipient .meta { font-size: 12px; margin-top: 10px; line-height: 20px; }
  .date { position: absolute; right: 68px; top: 297px; font-size: 12px; }
  .date b { font-weight: 600; }

  .body-copy { position: absolute; left: 32px; top: 400px; width: 750px; font-size: 12px; line-height: 20.5px; text-align: justify; }
  .body-copy p { margin-bottom: 20.5px; }
  .body-copy .soft { color: var(--muted); }
  .body-copy .firm { color: #333; }

  .signature { position: absolute; right: 68px; top: 852px; width: 168px; text-align: center; }
  .signature-mark { height: 44px; margin: 0 12px 8px; background: linear-gradient(90deg, #eef2f7, #dde5ef); border-radius: 4px; }
  .signature-line { border-top: 1px solid var(--pool-dark); }
  .signature-role { font-size: 12px; font-weight: 600; letter-spacing: 2.4px; color: var(--pool-dark); margin-top: 14px; }

  .footer { position: absolute; left: 32px; right: 32px; bottom: 34px; }
  .slogan { font-family: "Petit Formal Script", cursive; font-size: 17px; color: var(--pool-dark);
    letter-spacing: 1px; text-align: right; margin-bottom: 12px; }
  .footer-rule { display: flex; height: 3px; }
  .footer-rule .light { flex: 1; background: var(--pool-light); }
  .footer-rule .dark { width: 140px; background: var(--pool-dark); margin-left: 6px; }
</style>
</head>
<body>
  <main class="letterhead">
    <header>
      <div class="brand">
        <span class="brand-dot"></span>
        <span class="brand-name">Marc Doyle Pool Care</span>
      </div>
      <ul class="contact">
        <li><svg viewBox="0 0 10 10"><path d="M5 0a3.5 3.5 0 0 0-3.5 3.5C1.5 6 5 10 5 10s3.5-4 3.5-6.5A3.5 3.5 0 0 0 5 0zm0 5a1.4 1.4 0 1 1 0-2.8A1.4 1.4 0 0 1 5 5z"/></svg>P.O. Box 58, Cedar Hollow NY 11592</li>
        <li><svg viewBox="0 0 10 10"><path d="M2 0l2 2.4-1 1.2a6 6 0 0 0 3.4 3.4l1.2-1L10 8 8.6 10C4 10 0 6 0 1.4z"/></svg>(631) 529-6180</li>
        <li><svg viewBox="0 0 10 10"><path d="M0 2h10v1L5 6 0 3zM0 4l5 3 5-3v4H0z"/></svg>marcdoylewater@mailbrook.net</li>
      </ul>
      <div class="licensed">LICENSED &amp; INSURED</div>
    </header>

    <section class="recipient">
      <div class="to">To</div>
      <div class="name">Owen Hale</div>
      <div class="meta">CEO, BRIGHTLANE CO<br>M: +91 70215 44236</div>
    </section>
    <div class="date"><b>Date:</b> 24-03-2018</div>

    <article class="body-copy">
      <p class="soft">Lorem ipsum dolor sit amet, consectetur adipiscing elit. Pellentesque dictum, ante non ullamcorp er convallis, nunc quam blandit metus, ac mollis eros felis a orci. Donec congue, mauris ut pulvinar lobortis, dolor massa feugiat nisi, at tincidunt metus leo vel elit. Proin facilisis semper lobortis. Vivamus augue purus, cursus quis urna non, accumsan pellentesque est. Nulla in iaculis magna, quis aliqu et ex. Cras efficitur metus eget purus euismod facilisis. Proin non metus tincidunt, auctor ipsum a, tempor mi.</p>
      <p class="firm">Nulla egestas vulputate risus, ut vestibulum diam commodo id. Mauris ornare libero eu erat portt itor ultrices. Proin sed lectus scelerisque ligula bibendum sagittis ac nec leo. Donec ac accumsan diam, et lobortis mauris.</p>
      <p class="firm">Nulla congue volutpat nisl ac lobortis. Integer dignissim interdum libero, quis feugiat velit pretium at. Phasellus sit amet libero rutrum, feugiat odio et, tempus purus. Cras ultricies, leo at fringilla solli cit udin, leo sapien placerat enim, a rutrum lorem enim ut tortor. Phasellus magna ante, cong ue maximus egestas sit amet, venenatis scelerisque felis.</p>
      <p class="soft">Nulla congue volutpat nisl ac lobortis. Integer dignissim interdum libero, quis feugiat velit pretium at. Phasellus sit amet libero rutrum, feugiat odio et, tempus purus. Cras ultricies, leo at fringilla solli cit udin, leo sapien placerat enim, a rutrum lorem enim ut tortor. Phasellus magna ante, cong ue maximus egestas sit amet, venenatis scelerisque felis.</p>
      <p class="soft">Curabitur vitae urna volutpat, varius velit vehicula, fermentum magna. In maximus metus nunc, nec aliquet justo commodo eget. Nullam rhoncus vehicula gravida. Maecenas non sem at erat lacinia con vallis. Aliquam at lobortis erat.</p>
    </article>

    <div class="signature">
      <div class="signature-mark" role="img" aria-label="Handwritten signature of Owen Hale"></div>
      <div class="signature-line"></div>
      <div class="signature-role">PROPRIETOR</div>
    </div>

    <footer class="footer">
      <div class="slogan">Family Owned &amp; Operated for 25 Years</div>
      <div class="footer-rule"><span class="light"></span><span class="dark"></span></div>
    </footer>
  </main>
</body>
</html>
```